Halvering & Partners, LLC Business Card 2016

We need a new business card design for a very important trade show coming up.

We are a compliance Consulting Firm. Our clients are stock brokerage firms and investment advisers.

I would like our logo on both sides of the card.

Info in the front of the card shold include:

Logo
First & Last Name
Title
Office #
Cell #
Email
Company Address (42 W. Calloway Blvd., Suite 300 Corvale, WA 91847

Back of the card should include the logo and url: www.halveringpartnersgroup.com

Target Market(s)

Stock Brokerage Firms and Investment Advisers

Industry/Entity Type

Financial Service

Contact Information for Business Card

Russell K. Halvering
President
42 W. Calloway Blvd., Suite 300
Corvale, WA 91847
O 555.210.0147 ext. 204
C 555.340.0192
Email: russ@halveringpartnersgroup.com
www.halveringpartnersgroup.com

Requirements
Nice to have
• The back of the card could be black with the logo with the white letters.
• I do want the front of the card to at least have the color logo with the black "Halvering & Partners Lettering.

```html
<!DOCTYPE html>
<html lang="en">
<head>
<meta charset="utf-8">
<title>Halvering &amp; Partners — Business Card</title>
<link href="https://fonts.googleapis.com/css2?family=Kumbh+Sans:wght@400;600;700&display=swap" rel="stylesheet">
<style>
  :root {
    --backdrop: #d6d6d6;
    --card-white: #ffffff;
    --brand-red: #c8231c;
    --brand-red-dark: #a91a15;
    --ink-black: #0b0b0c;
    --ink-dark: #1c1c1c;
    --text-light: #f2f2f2;
    --divider: #2a2a2a;
  }
  * { margin: 0; padding: 0; box-sizing: border-box; }
  html, body {
    width: 1200px; height: 800px; overflow: hidden;
    background: var(--backdrop);
    font-family: "Kumbh Sans", sans-serif;
  }
  .canvas { position: relative; width: 1200px; height: 800px; }

  .card {
    position: absolute; top: 272px;
    height: 263px; overflow: hidden;
    background: var(--card-white);
  }

  /* Back side */
  .card--back { left: 62px; width: 515px; }
  .brand-lockup {
    position: absolute; left: 0; right: 0; top: 98px;
    display: flex; align-items: center; justify-content: center; gap: 16px;
  }
  .brand-lockup__mark {
    width: 52px; height: 52px; background: var(--brand-red);
  }
  .brand-lockup__name {
    font-weight: 600; font-size: 32px; color: var(--ink-dark);
    letter-spacing: 0.5px; line-height: 1;
  }

  /* Front side */
  .card--front { left: 642px; width: 471px; }
  .card__art { position: absolute; inset: 0; }
  .holder {
    position: absolute; left: 11px; top: 26px; color: var(--card-white);
  }
  .holder__name { font-weight: 700; font-size: 21px; line-height: 1.1; }
  .holder__title { font-weight: 400; font-size: 14px; line-height: 1.2; }

  .contact { position: absolute; left: 0; top: 104px; list-style: none; }
  .contact__item {
    position: relative; padding-left: 43px;
    color: var(--text-light); font-size: 12px; line-height: 18px;
  }
  .contact__icon {
    position: absolute; left: 12px; top: 2px; width: 14px; height: 14px;
  }
  .contact__item--gap { margin-top: 7px; }

  .front-brand {
    position: absolute; left: 303px; top: 90px; width: 168px; height: 146px;
    display: flex; flex-direction: column; align-items: center; justify-content: center; gap: 10px;
  }
  .front-brand__mark { width: 30px; height: 30px; background: var(--brand-red); }
  .front-brand__name {
    font-weight: 600; font-size: 17px; color: var(--card-white);
    text-align: center; line-height: 1.15; letter-spacing: 0.4px;
  }
</style>
</head>
<body>
<main class="canvas">

  <section class="card card--back" aria-label="Card back">
    <div class="brand-lockup">
      <span class="brand-lockup__mark"></span>
      <span class="brand-lockup__name">Halvering &amp; Partners</span>
    </div>
  </section>

  <section class="card card--front" aria-label="Card front">
    <svg class="card__art" width="471" height="263" viewBox="0 0 471 263" aria-hidden="true">
      <defs>
        <linearGradient id="redBand" x1="0" y1="0" x2="1" y2="0">
          <stop offset="0" stop-color="#b81e18"/>
          <stop offset="0.5" stop-color="#d4291f"/>
          <stop offset="1" stop-color="#b51d17"/>
        </linearGradient>
        <linearGradient id="blackBand" x1="0" y1="0" x2="0" y2="1">
          <stop offset="0" stop-color="#050505"/>
          <stop offset="1" stop-color="#151515"/>
        </linearGradient>
      </defs>
      <path d="M0 0 H205 C235 0 248 28 265 50 C285 76 300 86 318 88 V90 H0 Z" fill="url(#redBand)"/>
      <rect x="0" y="90" width="471" height="146" fill="url(#blackBand)"/>
      <line x1="303" y1="98" x2="303" y2="228" stroke="var(--divider)" stroke-width="1"/>
      <rect x="0" y="236" width="471" height="27" fill="url(#redBand)"/>
    </svg>

    <div class="holder">
      <p class="holder__name">Russell K. Halvering</p>
      <p class="holder__title">President</p>
    </div>

    <ul class="contact">
      <li class="contact__item">
        <svg class="contact__icon" viewBox="0 0 14 14" aria-hidden="true"><rect x="4" y="1" width="6" height="12" rx="1" fill="none" stroke="var(--brand-red)" stroke-width="1.2"/><line x1="6" y1="11" x2="8" y2="11" stroke="var(--brand-red)"/></svg>
        O&nbsp; 555.210.0147 ext. 204
      </li>
      <li class="contact__item">C&nbsp; 555.340.0192</li>
      <li class="contact__item">
        <svg class="contact__icon" viewBox="0 0 14 14" aria-hidden="true"><rect x="1" y="3" width="12" height="8" fill="none" stroke="var(--brand-red)" stroke-width="1.2"/><path d="M1 3 L7 8 L13 3" fill="none" stroke="var(--brand-red)" stroke-width="1.2"/></svg>
        russ@halveringpartnersgroup.com
      </li>
      <li class="contact__item contact__item--gap">
        <svg class="contact__icon" viewBox="0 0 14 14" aria-hidden="true"><rect x="1" y="2" width="12" height="8" fill="none" stroke="var(--brand-red)" stroke-width="1.2"/><line x1="5" y1="12.5" x2="9" y2="12.5" stroke="var(--brand-red)" stroke-width="1.2"/></svg>
        www.halveringpartnersgroup.com
      </li>
      <li class="contact__item contact__item--gap">
        <svg class="contact__icon" viewBox="0 0 14 14" aria-hidden="true"><path d="M7 13 C3 8 3 6.5 3 5.5 A4 4 0 0 1 11 5.5 C11 6.5 11 8 7 13 Z" fill="none" stroke="var(--brand-red)" stroke-width="1.2"/><circle cx="7" cy="5.5" r="1.4" fill="var(--brand-red)"/></svg>
        42 W. Calloway Blvd., Suite 300
      </li>
      <li class="contact__item">Corvale, WA 91847</li>
    </ul>

    <div class="front-brand">
      <span class="front-brand__mark"></span>
      <span class="front-brand__name">Halvering<br>&amp; Partners</span>
    </div>
  </section>

</main>
</body>
</html>
```